Bussiness card/stationary for healthcare consulting company
Keltova Healthcare Solutions
Use same font as used in my logo
Franklin Gothic Demi Cond
Professional
Daniel Prescott
CEO
5183 NE Bellcourt Lane
Topeka, KS 66609-2871
785-461-xxxx
dprescott@keltova.org
keltova.org
Please have the name, title, address, phone, etc. be fields that can be editted for updates and others needing business cards. I would like to be able to edit everything on the card except the logo and design. I need business cards, stationary and envelopes.

```html
<!DOCTYPE html>
<html lang="en">
<head>
<meta charset="utf-8">
<title>Keltova Healthcare Solutions – Stationery Set</title>
<link rel="stylesheet" href="https://fonts.googleapis.com/css2?family=Fira+Sans+Condensed:wght@400;600&family=Open+Sans:wght@400;600&display=swap">
<style>
  :root{
    --teal:#2f6f70;
    --teal-dark:#1f4f52;
    --teal-light:#5f9a99;
    --grey:#8a8d90;
    --grey-light:#c9cbcd;
    --ink:#4a4d50;
    --paper:#ffffff;
    --bg:#e9eaeb;
    --brand-font:"Fira Sans Condensed", "Arial Narrow", sans-serif;
    --body-font:"Open Sans", Arial, sans-serif;
  }
  *{box-sizing:border-box;margin:0;padding:0}
  html,body{width:1200px;height:866px;overflow:hidden}
  body{background:var(--bg);font-family:var(--body-font);color:var(--ink);position:relative}
  .sheet,.envelope,.card{position:absolute;background:var(--paper);box-shadow:0 2px 8px rgba(0,0,0,.15);overflow:hidden}

  /* brand lockup */
  .brand{display:flex;align-items:center;gap:6px;font-family:var(--brand-font);font-weight:600;color:var(--teal);line-height:1}
  .brand-dot{width:18px;height:18px;border-radius:50%;background:var(--teal);flex:none}
  .brand-name{font-size:20px;letter-spacing:.5px}
  .brand-tag{display:block;font-size:7px;letter-spacing:1.2px;margin-top:2px}
  .brand.light{color:#fff}
  .brand.light .brand-dot{background:#fff}

  .address{font-size:6.5px;line-height:1.45;color:var(--grey)}

  /* fax sheet */
  .fax{left:40px;top:40px;width:300px;height:388px}
  .fax .brand{position:absolute;left:22px;top:26px}
  .fax .address{position:absolute;right:22px;top:22px;text-align:left}
  .fax-rule{position:absolute;left:22px;right:22px;top:64px;height:1px;background:var(--grey-light)}
  .fax-title{position:absolute;left:22px;top:74px;font-family:var(--brand-font);font-weight:600;font-size:30px;color:var(--teal)}
  .fax-table{position:absolute;left:22px;right:22px;top:112px;border-collapse:collapse;width:256px;font-size:6.5px}
  .fax-table td{border-bottom:1px solid var(--grey-light);height:14px;padding-left:3px}
  .fax-table td.label{width:40px;font-weight:600;color:var(--ink)}
  .fax-table tr:first-child td{background:var(--teal);color:#fff;border:0}
  .fax-options{position:absolute;left:22px;right:22px;top:222px;display:flex;justify-content:space-between;font-size:6px;color:var(--grey)}
  .fax-options span::before{content:"";display:inline-block;width:6px;height:6px;border:1px solid var(--grey);margin-right:3px;vertical-align:-1px}
  .fax-lines{position:absolute;left:22px;right:22px;top:244px;height:110px;background:repeating-linear-gradient(to bottom,transparent 0 13px,#eceded 13px 14px)}
  .sheet-foot{position:absolute;left:22px;bottom:12px;font-size:6px;color:var(--grey)}

  /* letterhead */
  .letter{left:370px;top:40px;width:300px;height:388px}
  .letter .brand{position:absolute;left:22px;top:26px}
  .letter .address{position:absolute;right:22px;top:22px}
  .letter-body{position:absolute;left:22px;right:22px;top:78px;font-size:6px;line-height:1.6;color:var(--ink)}
  .letter-body p{margin-bottom:7px}
  .letter-body .salute{font-weight:600}
  .signature{width:70px;height:18px;background:linear-gradient(90deg,#d6d8da,#eef0f1);border-radius:2px;margin:4px 0 6px}

  /* envelopes */
  .env-front{left:700px;top:40px;width:460px;height:200px}
  .env-front .brand{position:absolute;left:24px;top:56px}
  .env-front .address{position:absolute;left:24px;top:96px}
  .env-back{left:700px;top:262px;width:460px;height:200px;background:linear-gradient(#d9dbdc,#f3f4f4)}
  .env-back svg,.env-front svg{position:absolute;left:0;top:0}

  /* business cards */
  .card{width:280px;height:160px;top:560px}
  .card-front{left:60px;background:linear-gradient(135deg,var(--teal-light),var(--teal-dark))}
  .card-front .brand,.card-grey .brand{position:absolute;left:50%;top:50%;transform:translate(-50%,-50%)}
  .card-front .brand-name,.card-grey .brand-name{font-size:26px}
  .card-front .brand-tag,.card-grey .brand-tag{font-size:8px}
  .card-back{left:460px}
  .card-back .brand{position:absolute;left:16px;top:18px}
  .card-back .brand-name{font-size:16px}
  .card-back .brand-tag{font-size:6px}
  .card-person{position:absolute;left:150px;top:18px;font-size:7px;line-height:1.5;color:var(--ink)}
  .card-person .name{font-family:var(--brand-font);font-weight:600;font-size:12px;color:var(--teal)}
  .card-person .title{font-size:7px;color:var(--grey);margin-bottom:6px}
  .card-band{position:absolute;left:0;right:0;bottom:0;height:22px;background:var(--teal)}
  .card-grey{left:860px;background:linear-gradient(135deg,#b5b8ba,#6e7275)}
</style>
</head>
<body>

<!-- Fax cover sheet -->
<section class="sheet fax">
  <div class="brand"><span class="brand-dot"></span><span><span class="brand-name">KELTOVA</span><span class="brand-tag">HEALTHCARE SOLUTIONS</span></span></div>
  <div class="address">5183 NE Bellcourt Lane<br>Topeka, KS 66609-2871<br>785-461-xxxx<br>keltova.org</div>
  <div class="fax-rule"></div>
  <h1 class="fax-title">FAX</h1>
  <table class="fax-table">
    <tr><td class="label">To</td><td></td><td class="label">Date</td><td></td></tr>
    <tr><td class="label">From</td><td></td><td class="label">Pages</td><td></td></tr>
    <tr><td class="label">Company</td><td></td><td class="label">CC</td><td></td></tr>
    <tr><td class="label">Fax</td><td></td><td class="label">Phone</td><td></td></tr>
    <tr><td class="label">Re</td><td></td><td class="label"></td><td></td></tr>
  </table>
  <div class="fax-options"><span>Urgent</span><span>For Review</span><span>Please Comment</span><span>Please Reply</span></div>
  <div class="fax-lines"></div>
  <div class="sheet-foot">keltova.org</div>
</section>

<!-- Letterhead -->
<section class="sheet letter">
  <div class="brand"><span class="brand-dot"></span><span><span class="brand-name">KELTOVA</span><span class="brand-tag">HEALTHCARE SOLUTIONS</span></span></div>
  <div class="address">5183 NE Bellcourt Lane<br>Topeka, KS 66609-2871<br>785-461-xxxx<br>dprescott@keltova.org</div>
  <div class="letter-body">
    <p>17 Oct 2024</p>
    <p class="salute">Dear Mr. Alan Whitmore,</p>
    <p>We are pleased to share our updated service plan for the coming quarter. Our team has reviewed your current processes and prepared clear steps to improve patient care and office workflow.</p>
    <p>Please review the attached summary at your convenience. We welcome your questions and look forward to meeting with your staff to discuss timelines, costs and expected outcomes in detail.</p>
    <p>Thank you for your continued trust in our consulting services. We remain committed to helping your organization deliver safe, efficient and caring healthcare to every patient.</p>
    <p>Best Regards,</p>
    <div class="signature" role="img" aria-label="Handwritten signature"></div>
    <p>Daniel Prescott<br>CEO</p>
  </div>
  <div class="sheet-foot">keltova.org</div>
</section>

<!-- Envelope front -->
<section class="envelope env-front">
  <svg width="460" height="200" viewBox="0 0 460 200" aria-hidden="true">
    <path d="M0 0H460V26C320 46 140 46 0 26Z" fill="var(--teal)"/>
    <path d="M0 182C140 170 320 170 460 182V200H0Z" fill="var(--teal)"/>
  </svg>
  <div class="brand"><span class="brand-dot"></span><span><span class="brand-name">KELTOVA</span><span class="brand-tag">HEALTHCARE SOLUTIONS</span></span></div>
  <div class="address">5183 NE Bellcourt Lane<br>Topeka, KS 66609-2871<br>785-461-xxxx<br>keltova.org</div>
</section>

<!-- Envelope back -->
<section class="envelope env-back">
  <svg width="460" height="200" viewBox="0 0 460 200" aria-hidden="true">
    <path d="M0 0H460L240 96Q230 100 220 96Z" fill="var(--teal)"/>
    <path d="M0 200L200 110M460 200L260 110" stroke="#c4c7c9" stroke-width="1" fill="none"/>
  </svg>
</section>

<!-- Business card front -->
<section class="card card-front">
  <div class="brand light"><span class="brand-dot"></span><span><span class="brand-name">KELTOVA</span><span class="brand-tag">HEALTHCARE SOLUTIONS</span></span></div>
</section>

<!-- Business card back -->
<section class="card card-back">
  <div class="brand"><span class="brand-dot"></span><span><span class="brand-name">KELTOVA</span><span class="brand-tag">HEALTHCARE SOLUTIONS</span></span></div>
  <div class="card-person">
    <div class="name">Daniel Prescott</div>
    <div class="title">CEO</div>
    5183 NE Bellcourt Lane<br>
    Topeka, KS 66609-2871<br>
    785-461-xxxx<br>
    dprescott@keltova.org<br>
    keltova.org
  </div>
  <div class="card-band"></div>
</section>

<!-- Business card alternate -->
<section class="card card-grey">
  <div class="brand light"><span class="brand-dot"></span><span><span class="brand-name">KELTOVA</span><span class="brand-tag">HEALTHCARE SOLUTIONS</span></span></div>
</section>

</body>
</html>
```